Stationery Set for new venture capital firm

We need a new set of stationery including letterhead, business cards, envelopes, with compliment slips for our new startup venture capital firm known as Halvorn.
We make alternative investments globally and hope to have a worldwide network of offices later.

The stationery should be elegant and not too fussy with the use of too many colors.

Venture Capital

```html
<!DOCTYPE html>
<html lang="en">
<head>
<meta charset="utf-8">
<title>Halvorn Stationery</title>
<link rel="stylesheet" href="https://fonts.googleapis.com/css2?family=Varela+Round&family=Roboto:wght@400&display=swap">
<style>
  :root {
    --page: #ffffff;
    --backdrop: #f4f5f6;
    --brand-blue: #00aeef;
    --brand-blue-light: #19bdf2;
    --tint: #e1f2fb;
    --logo-grey: #858585;
    --small-grey: #8a8a8a;
    --white: #ffffff;
    --edge: #c9c9c9;
  }
  html, body {
    margin: 0;
    padding: 0;
    width: 1200px;
    height: 901px;
    overflow: hidden;
    background: var(--backdrop);
  }
  .stationery {
    position: relative;
    width: 1200px;
    height: 901px;
  }
  .card {
    position: absolute;
    width: 480px;
    height: 290px;
    border-radius: 38px;
    overflow: hidden;
    box-sizing: border-box;
  }
  .card--front {
    left: 70px;
    top: 150px;
    background: var(--page);
    border: 1px solid var(--edge);
    display: flex;
    align-items: center;
    justify-content: center;
  }
  .card--back {
    left: 70px;
    top: 480px;
    background: var(--brand-blue);
  }
  .wordmark {
    font-family: "Varela Round", sans-serif;
    color: var(--logo-grey);
    font-weight: 400;
    letter-spacing: 0.5px;
    display: flex;
    align-items: center;
    gap: 12px;
  }
  .wordmark__dot {
    display: inline-block;
    border-radius: 50%;
    background: var(--brand-blue);
  }
  .card--front .wordmark { font-size: 46px; }
  .card--front .wordmark__dot { width: 26px; height: 26px; }
  .card__motif {
    position: absolute;
    right: -70px;
    top: -30px;
    width: 260px;
    height: 260px;
    border-radius: 50%;
    background: var(--brand-blue-light);
  }
  .contact {
    font-family: "Roboto", sans-serif;
    position: absolute;
    margin: 0;
  }
  .card--back .contact {
    left: 40px;
    top: 38px;
    color: var(--white);
    font-size: 13px;
    line-height: 17px;
  }
  .contact__group { margin: 0 0 18px; }
  .contact__web { margin-top: 6px; }
  .letterhead {
    position: absolute;
    left: 628px;
    top: 88px;
    width: 545px;
    height: 772px;
    background: var(--page);
    border: 1px solid var(--edge);
    box-sizing: border-box;
    overflow: hidden;
  }
  .letterhead .wordmark {
    position: absolute;
    left: 36px;
    top: 82px;
    font-size: 27px;
    gap: 8px;
  }
  .letterhead .wordmark__dot { width: 15px; height: 15px; }
  .letterhead .contact {
    left: 446px;
    top: 30px;
    color: var(--small-grey);
    font-size: 6.5px;
    line-height: 8.5px;
  }
  .letterhead .contact__group { margin-bottom: 9px; }
  .letterhead__motif {
    position: absolute;
    left: 372px;
    top: 238px;
    width: 360px;
    height: 360px;
    border-radius: 50%;
    background: var(--tint);
  }
  .letterhead__motif-band {
    position: absolute;
    left: 372px;
    top: 418px;
    width: 200px;
    height: 360px;
    background: var(--tint);
  }
</style>
</head>
<body>
<main class="stationery">
  <section class="card card--front" aria-label="Business card front">
    <div class="wordmark"><span class="wordmark__dot"></span>Halvorn</div>
  </section>

  <section class="card card--back" aria-label="Business card back">
    <div class="card__motif"></div>
    <address class="contact" style="font-style:normal">
      <p class="contact__group">12th Floor<br>Meridian Tower Offices<br>88 Quay Street, Harbourside<br>Hong Kong</p>
      <p class="contact__group">Tel +852 27403318<br>Fax +852 2740 3319</p>
      <p class="contact__group contact__web">www.halvorngroup.com</p>
    </address>
  </section>

  <section class="letterhead" aria-label="Letterhead">
    <div class="letterhead__motif"></div>
    <div class="letterhead__motif-band"></div>
    <div class="wordmark"><span class="wordmark__dot"></span>Halvorn</div>
    <address class="contact" style="font-style:normal">
      <p class="contact__group">12th Floor<br>Meridian Tower Offices<br>88 Quay Street, Harbourside<br>Hong Kong</p>
      <p class="contact__group">Tel +852 27403318<br>Fax +852 2740 3319</p>
      <p class="contact__group">www.halvorngroup.com</p>
    </address>
  </section>
</main>
</body>
</html>
```